EILT: Landing Page - EXPRESS VERSAND
Zielgruppe
Es soll in kurzer Zeit (max 48 Stunden) eine kleine Ladingpage entstehen. Expressversand / Import von China nach Deutschland . Aufgrund der stark steigenden Luftfrachtraten aus China heraus hat sich unsere Firma Fracht-Kapazitäten gesichert. Diese sollen nun angeboten werden. Über eine Ladingpage sollen Anfragen generiert werden. Diese Anfragen werden dann mit einem Angebot von uns beantwortet. Expressversand / Import von China nach Deutschland
Aufgabenstellung
Die Seite soll beinhalten:
- 1-2 Bilder (z. B. Luftfracht, Logistik, Flugzeug, Cargo, etc)
- kurzer erklärender Text: z.B. 'jetzt Angebot anfordern und günstig aus China per Express versenden.' Inkl. Abholung, Verzollung und Zustellung. Kurze Laufzeit von nur 3-5 Tagen. ab 45€ / Paket
- Anfrage Formular, bestehend aus: , Abholadresse in China/Post Code, ZielAdresse Deutschland, Sendungsinformationen (wie viele Kartons, wie schwer ist ein Karton und welche Abmessungen L/B/H ), wann ist die Sendung in China abholbereit, optional: Sendungsinhalt (Ware, Zolltarifnummer/HS Code) , Firma, Name, email adresse
- optional ein Header/Laufband etc mit: Bis zum 19. Nov 21 versenden - Ware bis MegaSonntag erhalten!
- 24h Servicehotline, Tel: 0987/314265
- 2-3 Kundenreferenzen: Bilder von Personen mit Text : „Schneller Versand - nur 4 Tage Laufzeit“ , „1A Service, ohne Probleme“ , „gute Preise - nur zu empfehlen.“
Unser Firmenlogo kann - muss aber nicht auftauchen.
In der farblichen Gestaltung haben Sie freie Hand und freuen uns auf Ihre Vorschläge.
Aufgrund der Dringlichkeit sollte diese Landingpage innerhalb 48 Stunden 'live ' gehen.
WICHTIG: Die Page sollte von Ihnen auch veröffentlich werden. Aktuell nutzen wir den Kelvo Homepagebaukasten. Die Page kann aber auch durch andere Anbieter veröffentlicht werden , zb Pagerune

```html
<!DOCTYPE html>
<html lang="de">
<head>
<meta charset="utf-8">
<title>Luvento – Expressversand China nach Deutschland</title>
<link href="https://fonts.googleapis.com/css2?family=Source+Sans+3:wght@400;600;700&display=swap" rel="stylesheet">
<style>
:root{
  --violet:#6d14ee;
  --rust:#c94b33;
  --ink:#3b22b8;
  --accent:#c8472f;
  --circle:#4122b8;
  --white:#ffffff;
  --field-border:#6b6b6b;
  --text:#2b2b2b;
}
*{box-sizing:border-box;margin:0;padding:0}
html,body{width:1200px;height:1191px;overflow:hidden}
body{
  font-family:"Source Sans 3",sans-serif;
  background:linear-gradient(120deg,var(--violet) 0%,#8a25c4 45%,#b9414f 75%,var(--rust) 100%);
  position:relative;color:var(--white);
}
.brand{position:absolute;left:152px;top:34px;display:flex;align-items:center;gap:8px}
.brand-dot{width:22px;height:22px;border-radius:50%;background:#f07a6a}
.brand-name{font-size:24px;font-weight:700;color:var(--white)}
.headline{position:absolute;left:150px;top:152px;font-size:43px;line-height:44px;font-weight:700;letter-spacing:-.3px}
.hotline{position:absolute;left:153px;top:346px;width:276px;text-align:center}
.hotline-label{font-size:20px;font-weight:600;margin-left:16px}
.hotline-pill{margin-top:6px;height:46px;border-radius:23px;background:var(--accent);display:flex;align-items:center;padding-left:24px;gap:10px;font-size:30px;font-weight:700}
.hero-circle{position:absolute;left:618px;top:11px;width:428px;height:428px;border-radius:50%;background:var(--circle)}
.hero-visual{position:absolute;left:515px;top:80px;width:610px;height:315px;border-radius:30px;
  background:linear-gradient(90deg,#2d4a5e 0%,#c68b4f 55%,#e5e0da 100%);opacity:.9}
.pointer{position:absolute;left:192px;top:450px}
.quote-card{position:absolute;left:150px;top:473px;width:900px;height:390px;background:var(--white);border-radius:3px}
.offer{position:absolute;left:97px;top:22px;width:780px;font-size:22.5px;line-height:30px;font-weight:600;color:var(--ink)}
.offer em{font-style:normal;color:var(--accent)}
.fields{position:absolute;left:52px;top:128px;display:grid;grid-template-columns:249px 249px 249px;column-gap:27px;row-gap:17px}
.fields .field:nth-child(3n){margin-left:-5px}
.field{height:40px;border:1.5px solid var(--field-border);border-radius:4px;padding-left:16px;display:flex;align-items:center;font-size:13.5px;color:var(--text)}
.send{position:absolute;left:327px;top:311px;width:253px;height:41px;border-radius:21px;background:var(--accent);display:flex;align-items:center;justify-content:center;gap:10px;font-size:18px;font-weight:600;color:var(--white)}
.quote-mark{position:absolute;left:148px;top:880px;font-size:150px;line-height:1;font-weight:700;color:#5b1fa0;font-family:Georgia,serif}
.reviews-title{position:absolute;left:0;width:1200px;top:914px;text-align:center;font-size:29px;font-weight:600}
.reviews{position:absolute;left:153px;top:985px;display:flex;gap:14px}
.review{width:289px;height:126px;background:rgba(255,255,255,.1);text-align:center;padding-top:26px}
.review-text{font-size:15.5px}
.reviewer{display:flex;justify-content:center;align-items:center;gap:12px;margin-top:15px}
.avatar{width:55px;height:55px;border-radius:50%;background:linear-gradient(135deg,#6b4a3a,#2c2320)}
.reviewer-meta{text-align:left;font-size:13px}
.stars{color:#f5b324;font-size:12px;letter-spacing:1px}
.copyright{position:absolute;left:0;width:1200px;top:1126px;text-align:center;font-size:13px}
</style>
</head>
<body>
<div class="brand"><span class="brand-dot"></span><span class="brand-name">Luvento</span></div>

<h1 class="headline">Expressversand /<br>Import von China<br>nach Deutschland</h1>

<div class="hotline">
  <div class="hotline-label">24h Servicehotline</div>
  <div class="hotline-pill">
    <svg width="24" height="24" viewBox="0 0 24 24" fill="none" stroke="#fff" stroke-width="1.8"><path d="M5 3h4l2 5-2.5 1.5a11 11 0 0 0 6 6L16 13l5 2v4a2 2 0 0 1-2 2A17 17 0 0 1 3 5a2 2 0 0 1 2-2z"/><path d="M14 3a7 7 0 0 1 7 7M14 6.5a3.5 3.5 0 0 1 3.5 3.5"/></svg>
    <span>0987/314265</span>
  </div>
</div>

<div class="hero-circle"></div>
<div class="hero-visual" role="img" aria-label="Frachtflugzeug, Containerschiff, Gabelstapler mit Kartons und Lieferwagen"></div>

<svg class="pointer" width="50" height="110" viewBox="0 0 50 110" fill="none" stroke="#c8472f" stroke-width="4" stroke-linecap="round"><path d="M46 20C38 4 28 0 26 14 22 40 24 70 25 102"/><path d="M8 70 25 102 34 74"/></svg>

<section class="quote-card">
  <p class="offer">Jetzt Angebot anfordern und günstig aus China per Express versenden.' Inkl. Abholung, Verzollung und Zustellung. Kurze Laufzeit von nur <em>3-5 Tagen.</em><br>ab <em>45€ / Paket</em></p>
  <form class="fields">
    <div class="field">Firma</div>
    <div class="field">Name</div>
    <div class="field">Email Adresse</div>
    <div class="field">Abholadresse in China</div>
    <div class="field">Post Code</div>
    <div class="field">ZielAdresse Deutschland</div>
    <div class="field">Wie Viele Kartons</div>
    <div class="field">Karton Gewicht</div>
    <div class="field">Abmessungen&nbsp; L / W / H</div>
  </form>
  <div class="send">
    <svg width="18" height="18" viewBox="0 0 24 24" fill="none" stroke="#fff" stroke-width="1.6"><path d="M22 2 2 11l8 3 3 8z"/><path d="M22 2 10 14"/></svg>
    <span>SENDEN</span>
  </div>
</section>

<div class="quote-mark">“</div>
<h2 class="reviews-title">Was under Kunde sagt</h2>

<div class="reviews">
  <div class="review">
    <p class="review-text">Schneller Versand - nur 4 Tage Laufzeit</p>
    <div class="reviewer"><div class="avatar" role="img" aria-label="Porträtfoto des Kunden"></div><div class="reviewer-meta">Malte Brink<div class="stars">★★★★★</div></div></div>
  </div>
  <div class="review">
    <p class="review-text">1A Service, ohne Probleme</p>
    <div class="reviewer"><div class="avatar" role="img" aria-label="Porträtfoto des Kunden"></div><div class="reviewer-meta">Jonas Velk<div class="stars">★★★★★</div></div></div>
  </div>
  <div class="review">
    <p class="review-text">Gute Preise - nur zu empfehlen.</p>
    <div class="reviewer"><div class="avatar" role="img" aria-label="Porträtfoto des Kunden"></div><div class="reviewer-meta">Malte Brink<div class="stars">★★★★★</div></div></div>
  </div>
</div>

<p class="copyright">Copyright 2021. Alle Rechte vorbehalten.</p>
</body>
</html>
```